Velbrook App Homepage Design making customers feel in control of their spend

Hi,
We need a App Homepage design with a UI similar to the attached mock up on an Quillo 4. The app is intended to put customers in control of their usage and spend on their fixed phone, broadband, mobile, gas and electricity.

Please fee free to propose improvements to the background images, icons, colours, etc.

Any questions please let me know.

Thanks
Tomasz

Target Market(s)

Consumer customers

Industry/Entity Type

Internet

Font styles to use
Sans Serif

Colors
3276b5
0255a3
85acd3
cfdeed
ffffff

Requirements
Must have
• Content in line with the guidelines in the attached mock up

```html
<!DOCTYPE html>
<html lang="en">
<head>
<meta charset="utf-8">
<title>Velbrook App Homepage</title>
<link rel="stylesheet" href="https://fonts.googleapis.com/css2?family=Roboto:wght@300;400;700&display=swap">
<style>
  :root {
    --stage: #fec572;
    --screen-top: #1c4c7e;
    --screen-mid: #174677;
    --screen-bottom: #143f6c;
    --white: #ffffff;
    --greeting: #b4c735;
    --electricity: #4b80c2;
    --gas: #c84f4a;
    --mobile: #8cb94b;
    --internet: #7965a9;
    --calls: #48a8c8;
    --photo-a: #a9b8a3;
    --photo-b: #6f5a4c;
  }
  * { box-sizing: border-box; margin: 0; padding: 0; }
  html, body { width: 1200px; height: 900px; overflow: hidden; }
  body {
    background: var(--stage);
    font-family: "Roboto", sans-serif;
    position: relative;
  }
  .app-screen {
    position: absolute;
    top: 72px;
    width: 415px;
    height: 737px;
    background: radial-gradient(circle at 30% 35%, var(--screen-top), var(--screen-mid) 55%, var(--screen-bottom));
    box-shadow: 3px 4px 6px rgba(0,0,0,0.22);
    overflow: hidden;
  }
  .app-screen--left { left: 173px; }
  .app-screen--right {
    left: 613px;
    background: radial-gradient(circle at 70% 40%, #1f5285, var(--screen-mid) 50%, var(--screen-bottom));
  }
  .screen-art { position: absolute; inset: 0; }
  .profile-photo {
    position: absolute;
    left: 140px;
    top: 107px;
    width: 135px;
    height: 134px;
    border: 4px solid var(--white);
    border-radius: 12px;
    background: linear-gradient(135deg, var(--photo-a), var(--photo-b));
  }
  .brand-name { font-size: 30px; font-weight: 400; fill: var(--white); }
  .greeting { font-size: 19px; font-weight: 700; fill: var(--greeting); }
  .welcome { font-size: 19px; font-weight: 300; fill: var(--white); }
  .support-hours { font-size: 36px; font-weight: 700; fill: var(--white); }
  .support-label { font-size: 17px; font-weight: 700; fill: var(--white); }
  .charges-label { font-size: 19px; font-weight: 300; fill: var(--white); }
  .charges-total { font-size: 18px; font-weight: 700; fill: var(--white); }
  .service-label { font-size: 13px; font-weight: 300; fill: var(--white); }
  .bill-note { font-size: 13px; font-weight: 300; fill: var(--white); }
  .seg { fill: none; stroke-width: 22; }
  .icon-ring { fill: none; stroke-width: 2; }
</style>
</head>
<body>

<section class="app-screen app-screen--left" aria-label="Velbrook home screen">
  <div class="profile-photo" role="img" aria-label="Profile photo of the customer"></div>
  <svg class="screen-art" width="415" height="737" viewBox="0 0 415 737">
    <circle cx="52" cy="50" r="14" fill="var(--calls)"/>
    <text class="brand-name" x="74" y="61">Velbrook</text>
    <g class="menu-icon" fill="var(--white)">
      <rect x="350" y="38" width="36" height="5" rx="2.5"/>
      <rect x="350" y="49" width="36" height="5" rx="2.5"/>
      <rect x="350" y="60" width="36" height="5" rx="2.5"/>
    </g>
    <text class="greeting" x="208" y="272" text-anchor="middle">Good Morning Maren</text>
    <text class="welcome" x="208" y="295" text-anchor="middle">WELCOME TO VELBROOK</text>
    <text class="support-hours" x="208" y="347" text-anchor="middle">24/7</text>
    <text class="support-label" x="208" y="366" text-anchor="middle">SUPPORT</text>

    <g class="charges-ring" transform="rotate(-90 208 483)">
      <circle class="seg" cx="208" cy="483" r="89" pathLength="360" stroke="var(--electricity)" stroke-dasharray="129 360" stroke-dashoffset="-2"/>
      <circle class="seg" cx="208" cy="483" r="89" pathLength="360" stroke="var(--gas)" stroke-dasharray="100 360" stroke-dashoffset="-134"/>
      <circle class="seg" cx="208" cy="483" r="89" pathLength="360" stroke="var(--mobile)" stroke-dasharray="51 360" stroke-dashoffset="-238"/>
      <circle class="seg" cx="208" cy="483" r="89" pathLength="360" stroke="var(--internet)" stroke-dasharray="15 360" stroke-dashoffset="-293"/>
      <circle class="seg" cx="208" cy="483" r="89" pathLength="360" stroke="var(--calls)" stroke-dasharray="46 360" stroke-dashoffset="-311"/>
    </g>
    <text class="charges-label" x="208" y="465" text-anchor="middle">Your Current</text>
    <text class="charges-label" x="208" y="488" text-anchor="middle">Total Charges</text>
    <text class="charges-total" x="208" y="511" text-anchor="middle">£68.39</text>

    <g class="service service--calls">
      <circle class="icon-ring" cx="130" cy="367" r="17" stroke="var(--calls)"/>
      <path d="M123 359 q2-2 4 0 l2 4 q0 2-2 3 q2 4 5 6 q1-2 3-2 l4 2 q2 2 0 4 q-3 3-7 1 q-7-4-10-11 q-1-4 1-7z" fill="var(--calls)"/>
      <text class="service-label" x="130" y="402" text-anchor="middle">Calls</text>
    </g>
    <g class="service service--internet" stroke="var(--internet)" fill="none" stroke-width="1.5">
      <circle class="icon-ring" cx="77" cy="453" r="17"/>
      <circle cx="77" cy="453" r="11"/>
      <ellipse cx="77" cy="453" rx="5" ry="11"/>
      <line x1="66" y1="453" x2="88" y2="453"/>
      <line x1="68" y1="447" x2="86" y2="447"/>
      <line x1="68" y1="459" x2="86" y2="459"/>
      <text class="service-label" x="77" y="487" text-anchor="middle" stroke="none">Internet</text>
    </g>
    <g class="service service--electricity">
      <circle class="icon-ring" cx="345" cy="442" r="17" stroke="var(--electricity)"/>
      <rect x="338" y="437" width="14" height="10" rx="2" fill="var(--electricity)"/>
      <rect x="340" y="431" width="2.5" height="7" fill="var(--electricity)"/>
      <rect x="347.5" y="431" width="2.5" height="7" fill="var(--electricity)"/>
      <rect x="343.5" y="446" width="3" height="8" fill="var(--electricity)"/>
      <text class="service-label" x="345" y="476" text-anchor="middle">Electricity</text>
    </g>
    <g class="service service--mobile">
      <circle class="icon-ring" cx="93" cy="542" r="17" stroke="var(--mobile)"/>
      <rect x="87" y="532" width="12" height="20" rx="2" fill="none" stroke="var(--mobile)" stroke-width="1.5"/>
      <line x1="91" y1="549" x2="95" y2="549" stroke="var(--mobile)" stroke-width="1.5"/>
      <text class="service-label" x="93" y="576" text-anchor="middle">Mobile</text>
    </g>
    <g class="service service--gas">
      <circle class="icon-ring" cx="209" cy="615" r="17" stroke="var(--gas)"/>
      <path d="M209 604 q7 7 5 13 q-1 4-5 4 q-4 0-5-4 q-1-4 3-7 q0 3 2 4 q1-5 0-10z" fill="var(--gas)"/>
      <rect x="200" y="622" width="18" height="2" fill="var(--gas)"/>
      <text class="service-label" x="209" y="649" text-anchor="middle">Gas</text>
    </g>

    <text class="bill-note" x="208" y="685" text-anchor="middle">Last Bill: £75.76 on 9/12/2016</text>
    <text class="bill-note" x="208" y="702" text-anchor="middle">Allowance renews in 18 days</text>
  </svg>
</section>

<section class="app-screen app-screen--right" aria-label="Velbrook home screen, alternative background">
  <div class="profile-photo" role="img" aria-label="Profile photo of the customer"></div>
  <svg class="screen-art" width="415" height="737" viewBox="0 0 415 737">
    <circle cx="52" cy="50" r="14" fill="var(--calls)"/>
    <text class="brand-name" x="74" y="61">Velbrook</text>
    <g class="menu-icon" fill="var(--white)">
      <rect x="350" y="38" width="36" height="5" rx="2.5"/>
      <rect x="350" y="49" width="36" height="5" rx="2.5"/>
      <rect x="350" y="60" width="36" height="5" rx="2.5"/>
    </g>
    <text class="greeting" x="208" y="272" text-anchor="middle">Good Morning Maren</text>
    <text class="welcome" x="208" y="295" text-anchor="middle">WELCOME TO VELBROOK</text>
    <text class="support-hours" x="208" y="347" text-anchor="middle">24/7</text>
    <text class="support-label" x="208" y="366" text-anchor="middle">SUPPORT</text>

    <g class="charges-ring" transform="rotate(-90 208 483)">
      <circle class="seg" cx="208" cy="483" r="89" pathLength="360" stroke="var(--electricity)" stroke-dasharray="129 360" stroke-dashoffset="-2"/>
      <circle class="seg" cx="208" cy="483" r="89" pathLength="360" stroke="var(--gas)" stroke-dasharray="100 360" stroke-dashoffset="-134"/>
      <circle class="seg" cx="208" cy="483" r="89" pathLength="360" stroke="var(--mobile)" stroke-dasharray="51 360" stroke-dashoffset="-238"/>
      <circle class="seg" cx="208" cy="483" r="89" pathLength="360" stroke="var(--internet)" stroke-dasharray="15 360" stroke-dashoffset="-293"/>
      <circle class="seg" cx="208" cy="483" r="89" pathLength="360" stroke="var(--calls)" stroke-dasharray="46 360" stroke-dashoffset="-311"/>
    </g>
    <text class="charges-label" x="208" y="465" text-anchor="middle">Your Current</text>
    <text class="charges-label" x="208" y="488" text-anchor="middle">Total Charges</text>
    <text class="charges-total" x="208" y="511" text-anchor="middle">£68.39</text>

    <g class="service service--calls">
      <circle class="icon-ring" cx="130" cy="367" r="17" stroke="var(--calls)"/>
      <path d="M123 359 q2-2 4 0 l2 4 q0 2-2 3 q2 4 5 6 q1-2 3-2 l4 2 q2 2 0 4 q-3 3-7 1 q-7-4-10-11 q-1-4 1-7z" fill="var(--calls)"/>
      <text class="service-label" x="130" y="402" text-anchor="middle">Calls</text>
    </g>
    <g class="service service--internet" stroke="var(--internet)" fill="none" stroke-width="1.5">
      <circle class="icon-ring" cx="77" cy="453" r="17"/>
      <circle cx="77" cy="453" r="11"/>
      <ellipse cx="77" cy="453" rx="5" ry="11"/>
      <line x1="66" y1="453" x2="88" y2="453"/>
      <line x1="68" y1="447" x2="86" y2="447"/>
      <line x1="68" y1="459" x2="86" y2="459"/>
      <text class="service-label" x="77" y="487" text-anchor="middle" stroke="none">Internet</text>
    </g>
    <g class="service service--electricity">
      <circle class="icon-ring" cx="345" cy="442" r="17" stroke="var(--electricity)"/>
      <rect x="338" y="437" width="14" height="10" rx="2" fill="var(--electricity)"/>
      <rect x="340" y="431" width="2.5" height="7" fill="var(--electricity)"/>
      <rect x="347.5" y="431" width="2.5" height="7" fill="var(--electricity)"/>
      <rect x="343.5" y="446" width="3" height="8" fill="var(--electricity)"/>
      <text class="service-label" x="345" y="476" text-anchor="middle">Electricity</text>
    </g>
    <g class="service service--mobile">
      <circle class="icon-ring" cx="93" cy="542" r="17" stroke="var(--mobile)"/>
      <rect x="87" y="532" width="12" height="20" rx="2" fill="none" stroke="var(--mobile)" stroke-width="1.5"/>
      <line x1="91" y1="549" x2="95" y2="549" stroke="var(--mobile)" stroke-width="1.5"/>
      <text class="service-label" x="93" y="576" text-anchor="middle">Mobile</text>
    </g>
    <g class="service service--gas">
      <circle class="icon-ring" cx="209" cy="615" r="17" stroke="var(--gas)"/>
      <path d="M209 604 q7 7 5 13 q-1 4-5 4 q-4 0-5-4 q-1-4 3-7 q0 3 2 4 q1-5 0-10z" fill="var(--gas)"/>
      <rect x="200" y="622" width="18" height="2" fill="var(--gas)"/>
      <text class="service-label" x="209" y="649" text-anchor="middle">Gas</text>
    </g>

    <text class="bill-note" x="208" y="685" text-anchor="middle">Last Bill: £75.76 on 9/12/2016</text>
    <text class="bill-note" x="208" y="702" text-anchor="middle">Allowance renews in 18 days</text>
  </svg>
</section>

</body>
</html>
```